Business card design with slight adjustment to current logo
Marlow Heating Cooling & Plumbing
Business card design with slight adjustment to current logo - Trade
Creative Brief
Bright & Fun-filled
no name wanted on card
no title wanted on card
3167 Penwick Ave Findlay, OH 45893
marlowhvacfindlay@examplemail.test
marlow-hvac.test
Heating Cooling Plumbing The logo I have is an older logo, we want to keep it the same but the type of file I have it flat looking, plain colored. If the logo can be tweaked to look brighter, less flat, but very similar so as not to look much different I would appreciate that. My hope was to have the flame in the logo look a little more like a flame, I think maybe the curve of it is just a little off, making it more like a shark fin or something. for the logo and business card, that color blue in logo is a favorite.
Tkvorel42 Tkvorel42
Cards can also say: Service & Install Free Estimates
This is more me looking for business card designs, if the logo can be adjusted a little bit and you have the idea for it, fine. But mainly I need good business card designs for current logo

```html
<!DOCTYPE html>
<html lang="en">
<head>
<meta charset="utf-8">
<title>Marlow Heating Cooling &amp; Plumbing – Business Card</title>
<link rel="stylesheet" href="https://fonts.googleapis.com/css2?family=Montserrat:wght@500;800&display=swap">
<style>
  :root {
    --page-bg: #ffffff;
    --card-bg: #ffffff;
    --card-edge: #e6e9ee;
    --ink-dark: #3a3d42;
    --ink-mid: #2f3236;
    --brand-blue: #1f73c8;
    --brand-blue-deep: #1560ad;
    --brand-blue-light: #cfe3f6;
    --brand-blue-mist: #eaf3fb;
  }
  * { margin: 0; padding: 0; box-sizing: border-box; }
  html, body {
    width: 1200px;
    height: 871px;
    overflow: hidden;
    background: var(--page-bg);
  }
  .business-card {
    position: absolute;
    left: 50px;
    top: 124px;
    width: 1100px;
    height: 623px;
    background: var(--card-bg);
    border: 1px solid var(--card-edge);
    overflow: hidden;
  }
  .card-decoration {
    position: absolute;
    inset: 0;
    width: 100%;
    height: 100%;
  }
  .wordmark {
    position: absolute;
    left: 0;
    right: 0;
    top: 185px;
    text-align: center;
    font-family: "Montserrat", sans-serif;
    font-weight: 800;
    font-size: 140px;
    line-height: 1;
    letter-spacing: -2px;
    color: var(--ink-dark);
  }
  .service-line {
    position: absolute;
    left: 0;
    right: 0;
    top: 405px;
    display: flex;
    justify-content: center;
    gap: 30px;
    font-family: "Montserrat", sans-serif;
    font-weight: 500;
    font-size: 32px;
    letter-spacing: 1px;
    color: var(--ink-mid);
    list-style: none;
  }
  .service-line li {
    display: flex;
    align-items: center;
    gap: 14px;
  }
  .service-line li::before {
    content: "";
    width: 14px;
    height: 14px;
    border-radius: 50%;
    background: var(--ink-mid);
  }
</style>
</head>
<body>
  <main class="business-card">
    <svg class="card-decoration" viewBox="0 0 1100 623" aria-hidden="true">
      <defs>
        <linearGradient id="band-gradient" x1="0" y1="0" x2="1" y2="0">
          <stop offset="0" stop-color="#8fbde8"/>
          <stop offset="0.45" stop-color="#4a92d6"/>
          <stop offset="1" stop-color="#1560ad"/>
        </linearGradient>
        <linearGradient id="band-sheen" x1="0" y1="0" x2="1" y2="0">
          <stop offset="0" stop-color="#eaf3fb"/>
          <stop offset="1" stop-color="#bcd8f2"/>
        </linearGradient>
        <radialGradient id="corner-glow" cx="0.5" cy="0.5" r="0.5">
          <stop offset="0" stop-color="#cfe3f6"/>
          <stop offset="0.7" stop-color="#e3eef9"/>
          <stop offset="1" stop-color="#ffffff" stop-opacity="0"/>
        </radialGradient>
      </defs>
      <rect x="-160" y="300" width="560" height="440" fill="url(#corner-glow)" role="img" aria-label="Faint decorative flourish in pale blue"/>
      <path d="M0 560 C 300 520, 700 470, 1100 440 L 1100 470 C 700 500, 320 560, 0 600 Z" fill="url(#band-sheen)" opacity="0.8"/>
      <path d="M0 623 C 260 590, 640 520, 1100 478 L 1100 623 Z" fill="url(#band-gradient)"/>
    </svg>

    <h1 class="wordmark">MARLOW</h1>
    <ul class="service-line">
      <li>HEATING</li>
      <li>COOLING</li>
      <li>PLUMBING</li>
    </ul>
  </main>
</body>
</html>
```